Heron Renovation Group Postcard Design Project

I'm a General Contractor specializing in luxury residential remodeling.

THIS IS AN EDDM POSTCARD. THE ENTIRE BACK SIDE OF THE CARD WILL BE USED.

I FORGOT TO MENTION THIS IN MY ORIGINAL BRIEF.

Target Market(s)

OLD, rich people so please make sure the fonts are clear and crisp.

Font styles to use
Sans Serif

```html
<!DOCTYPE html>
<html lang="en">
<head>
<meta charset="utf-8">
<title>Heron Renovation Group – EDDM Postcard</title>
<link rel="stylesheet" href="https://fonts.googleapis.com/css2?family=Bebas+Neue&family=Oswald:wght@500&family=Lato:wght@400;700;900&display=swap">
<style>
  :root {
    --ink: #231f20;
    --panel-dark: #1f1d1e;
    --brand-red: #e31e2d;
    --orange: #f7941d;
    --orange-deep: #ec5a24;
    --yellow: #fbc531;
    --paper: #ffffff;
    --stage: #e6e6e6;
    --silver: #c9c9c9;
  }
  * { box-sizing: border-box; margin: 0; padding: 0; }
  html, body { width: 902px; height: 1200px; overflow: hidden; }
  body { background: var(--stage); position: relative; font-family: "Lato", sans-serif; }

  .card {
    position: absolute;
    width: 693px; height: 460px;
    background: var(--paper);
    transform: scale(0.97);
    transform-origin: top left;
    overflow: hidden;
    box-shadow: 0 4px 14px rgba(0,0,0,0.25);
  }
  .card--front { left: 46px; top: 120px; }
  .card--back { left: 162px; top: 638px; }
  .card svg.card-art { position: absolute; inset: 0; }

  .heading { font-family: "Bebas Neue", sans-serif; }
  .value-label { font-family: "Oswald", sans-serif; font-weight: 500; font-size: 13px; fill: var(--ink); }
  .contact-line { font-family: "Lato", sans-serif; font-weight: 700; fill: var(--ink); }
  .cta { font-family: "Lato", sans-serif; font-weight: 900; text-anchor: middle; }

  .brand-name {
    position: absolute;
    display: flex; align-items: center; gap: 8px;
    font-family: "Lato", sans-serif; font-weight: 900;
    color: var(--ink);
    white-space: nowrap;
  }
  .brand-name__mark { display: block; background: var(--brand-red); }
  .card--front .brand-name { left: 26px; top: 70px; font-size: 21px; }
  .card--front .brand-name__mark { width: 18px; height: 18px; }
  .card--back .brand-name { left: 383px; top: 52px; font-size: 15px; }
  .card--back .brand-name__mark { width: 13px; height: 13px; }

  .photo-house {
    position: absolute; left: 0; top: 150px; width: 330px; height: 310px;
    background: linear-gradient(180deg, #ffffff 0%, #cfd3d6 22%, #a99c8a 52%, #6e6558 70%, #4f7a33 82%, #3f6a2a 100%);
  }
  .photo-house--faded {
    left: 0; top: 0; width: 360px; height: 460px;
    background: linear-gradient(180deg, #f4f2ef 0%, #e8e4de 40%, #dcd8cf 70%, #cfd6c0 100%);
  }

  .about {
    position: absolute; left: 26px; top: 32px; width: 318px;
  }
  .about__title {
    font-family: "Lato", sans-serif; font-weight: 900; font-size: 14px;
    color: var(--brand-red); margin-bottom: 8px;
  }
  .about__text {
    font-size: 9.6px; line-height: 12.3px; color: var(--ink); text-align: justify;
  }
</style>
</head>
<body>

<!-- FRONT -->
<section class="card card--front">
  <div class="photo-house" role="img" aria-label="Photograph of a large two-storey luxury home with lit windows and a green lawn at dusk"></div>

  <svg class="card-art" viewBox="0 0 693 460" width="693" height="460">
    <defs>
      <radialGradient id="panelGrey" cx="55%" cy="45%" r="70%">
        <stop offset="0" stop-color="#ffffff"/>
        <stop offset="1" stop-color="#c4c4c4"/>
      </radialGradient>
      <linearGradient id="bandFront" x1="0" x2="1">
        <stop offset="0" stop-color="#e8362b"/>
        <stop offset="0.4" stop-color="#f7941d"/>
        <stop offset="1" stop-color="#fbc531"/>
      </linearGradient>
      <radialGradient id="coreFill" cx="45%" cy="35%" r="70%">
        <stop offset="0" stop-color="#fbb040"/>
        <stop offset="1" stop-color="#f26522"/>
      </radialGradient>
      <linearGradient id="ring" x1="0" y1="0" x2="1" y2="1">
        <stop offset="0" stop-color="#f2f2f2"/>
        <stop offset="0.5" stop-color="#8c8c8c"/>
        <stop offset="1" stop-color="#e0e0e0"/>
      </linearGradient>
      <marker id="arrowHead" viewBox="0 0 10 10" refX="5" refY="5" markerWidth="3.2" markerHeight="3.2" orient="auto">
        <path d="M0 0 L10 5 L0 10 Z" fill="#f7941d"/>
      </marker>
    </defs>

    <!-- headline block -->
    <rect class="header-band" x="330" y="0" width="363" height="130" fill="var(--panel-dark)"/>
    <rect class="header-ribbon" x="330" y="72" width="363" height="33" fill="var(--brand-red)"/>
    <text class="heading" x="342" y="64" font-size="41" fill="#fff">WE ARE SPECIALIZING IN</text>
    <text class="heading" x="342" y="100" font-size="31" fill="#fff">LUXURY RESIDENTIAL REMODELING</text>

    <!-- core values panel -->
    <rect class="values-panel" x="330" y="130" width="363" height="330" fill="url(#panelGrey)"/>

    <g class="value-arrows" stroke="#f7941d" stroke-width="7" marker-end="url(#arrowHead)">
      <line x1="452" y1="190" x2="412" y2="162"/>
      <line x1="550" y1="190" x2="594" y2="158"/>
      <line x1="431" y1="232" x2="392" y2="232"/>
      <line x1="570" y1="230" x2="612" y2="230"/>
      <line x1="450" y1="278" x2="412" y2="302"/>
      <line x1="550" y1="276" x2="590" y2="300"/>
    </g>

    <circle cx="500" cy="235" r="68" fill="url(#ring)"/>
    <circle cx="500" cy="235" r="60" fill="url(#coreFill)"/>
    <text class="heading" x="500" y="229" font-size="31" fill="var(--ink)" text-anchor="middle">OUR CORE</text>
    <text class="heading" x="500" y="266" font-size="31" fill="var(--ink)" text-anchor="middle">VALUES</text>

    <text class="value-label" x="344" y="151">HE CREATIVE PROCESS</text>
    <text class="value-label" x="543" y="151">EDUCATING OUR CLIENTS</text>
    <text class="value-label" x="337" y="228">INTEGRITY</text>
    <text class="value-label" x="616" y="225">HAVING FUN</text>
    <text class="value-label" x="392" y="313" text-anchor="middle">WORKS CLASS</text>
    <text class="value-label" x="392" y="331" text-anchor="middle">CUSTOMER SERVICE</text>
    <text class="value-label" x="628" y="302" text-anchor="middle">QUALITY</text>
    <text class="value-label" x="628" y="320" text-anchor="middle">CRAFTSMANSHIP</text>

    <!-- contact band -->
    <path class="swoosh" d="M345 460 C435 385 560 360 693 356 L693 368 C560 370 450 378 372 460 Z" fill="var(--panel-dark)"/>
    <path class="contact-band" d="M372 460 C450 378 560 370 693 368 L693 460 Z" fill="url(#bandFront)"/>

    <text class="contact-line" x="636" y="411" font-size="22" text-anchor="end">123-456-790</text>
    <text class="contact-line" x="636" y="427" font-size="12.5" text-anchor="end">youremailaddress.compantname.com</text>
    <text class="contact-line" x="636" y="442" font-size="12.5" text-anchor="end">www.websitename.com</text>

    <g class="contact-icons" fill="none" stroke="#fff" stroke-width="1.3">
      <circle cx="652" cy="404" r="5"/>
      <path d="M650 402 q1 4 4 4"/>
      <path d="M652 429 c-4 -4 -4 -8 0 -8 c4 0 4 4 0 8 Z" fill="#fff"/>
      <circle cx="652" cy="438" r="5"/>
      <line x1="647" y1="438" x2="657" y2="438"/>
    </g>

    <!-- call to action -->
    <circle cx="302" cy="410" r="78" fill="#fff"/>
    <circle cx="302" cy="410" r="72" fill="var(--panel-dark)"/>
    <text class="cta" x="302" y="397" font-size="22" fill="#fff">CONTACT</text>
    <text class="cta" x="302" y="422" font-size="22" fill="#fff">US</text>
    <text class="cta" x="302" y="443" font-size="16" fill="var(--brand-red)">TODAY!</text>
  </svg>

  <div class="brand-name"><span class="brand-name__mark"></span>Heron Renovation Group</div>
</section>

<!-- BACK -->
<section class="card card--back">
  <div class="photo-house photo-house--faded" role="img" aria-label="Faded photograph of a bright home entrance with white columns and lawn"></div>

  <svg class="card-art" viewBox="0 0 693 460" width="693" height="460">
    <defs>
      <linearGradient id="bandBack" x1="0" x2="1">
        <stop offset="0" stop-color="#fbc531"/>
        <stop offset="0.55" stop-color="#f7941d"/>
        <stop offset="1" stop-color="#ec5a24"/>
      </linearGradient>
      <linearGradient id="divider" x1="0" x2="1">
        <stop offset="0" stop-color="rgba(0,0,0,0.18)"/>
        <stop offset="1" stop-color="rgba(0,0,0,0)"/>
      </linearGradient>
    </defs>

    <rect class="divider-shadow" x="360" y="0" width="8" height="460" fill="url(#divider)"/>

    <text class="heading" x="20" y="240" font-size="42" fill="var(--brand-red)">WE ARE SPECIALIZING IN</text>
    <text class="heading" x="20" y="279" font-size="31" fill="var(--ink)">LUXURY RESIDENTIAL REMODELING</text>

    <path class="swoosh" d="M0 314 Q180 306 330 372 L330 392 Q180 336 0 342 Z" fill="var(--panel-dark)"/>
    <path class="contact-band" d="M0 342 Q180 336 330 392 L330 460 L0 460 Z" fill="url(#bandBack)"/>

    <g class="contact-icons" fill="none" stroke="#fff" stroke-width="1.3">
      <circle cx="27" cy="385" r="5"/>
      <path d="M25 383 q1 4 4 4"/>
      <path d="M27 411 c-4 -4 -4 -8 0 -8 c4 0 4 4 0 8 Z" fill="#fff"/>
      <circle cx="27" cy="424" r="5"/>
      <line x1="22" y1="424" x2="32" y2="424"/>
    </g>
    <text class="contact-line" x="40" y="394" font-size="24">123-456-790</text>
    <text class="contact-line" x="40" y="411" font-size="13">youremailaddress.compantname.com</text>
    <text class="contact-line" x="40" y="428" font-size="13">www.websitename.com</text>

    <circle cx="368" cy="400" r="78" fill="#fff"/>
    <circle cx="368" cy="400" r="72" fill="var(--panel-dark)"/>
    <text class="cta" x="368" y="390" font-size="22" fill="#fff">CONTACT</text>
    <text class="cta" x="368" y="415" font-size="22" fill="#fff">US</text>
    <text class="cta" x="368" y="436" font-size="16" fill="var(--brand-red)">TODAY!</text>

    <rect class="stamp-box" x="590" y="27" width="85" height="78" fill="#fff" stroke="#9a9a9a" stroke-width="1"/>
  </svg>

  <div class="about">
    <h2 class="about__title">ABOUT US :</h2>
    <p class="about__text">Lorem Ipsum is simply dummy text of the printing and typesetting industry. Lorem Ipsum has been the industry's standard dummy text ever since the 1500s, when an unknown printer took a galley of type and scrambled it to make a type specimen book. It has survived not only five centuries, but also the leap into electronic typesetting, remaining essentially unchanged. It was popularised in the 1960s with the release of Letraset sheets containing Lorem Ipsum passages, and more recently with desktop publishing software like Aldus PageMaker including versions of Lorem Ipsum.</p>
  </div>

  <div class="brand-name"><span class="brand-name__mark"></span>Heron Renovation Group</div>
</section>

</body>
</html>
```